Eco friendly Swedish beauty products sold in aluminum bottles - label design needed

We need help in designing a series of stick on labels for 80 ml (2.7 fl. oz.) aluminum bottles containing beauty products such as soaps, shampoo etc. The diameter of the bottle is 36 mm and the body of the bottles measures approx. 106 mm.
It is important for us that the label has a simplistic and clean feel with few colors (and the right ones!) and that the label helps amplify this product being both better and a more sustainable alternative to many of our plastic bottle competitors. The design and label should communicate the feel of an Eco-friendly, sustainable and modern brand of high quality - and with a Swedish concept.
We are using Montserrat font in our materials. Find attached information of preferred colors, the bottles and one example of our logotype. I am also available on e-mail should further information be needed.

Looking forward and very excited to receive your suggestions.
Note that we are expecting to start selling a series of approximately 10 different products where I will need one "master design" and then only smaller changes for each of the different products.

Target Market(s)

People whom are aware and not only look at price tag. Private and commercial market.

Industry/Entity Type

Beauty

Font styles to use
Other font styles liked:
• Montserrat

Requirements
Must have
• It must give the feel of being both better and a more sustainable alternative to many of our plastic bottle competitors.
Nice to have
• Simplistic. Clean. Clear.
Should not have
• Wrong colors, too complex designs.

```html
<!DOCTYPE html>
<html lang="en">
<head>
<meta charset="utf-8">
<title>Nordvik Care – Exfoliating Cleanser Label Series</title>
<link href="https://fonts.googleapis.com/css2?family=Montserrat:wght@300;400;500&display=swap" rel="stylesheet">
<style>
  :root {
    --canvas-bg: #d6d6d6;
    --ink: #1d2426;
    --white: #ffffff;
    --teal-top: #dff1f2;
    --teal-mid: #7fc0c4;
    --teal-bottom: #1d6a72;
    --olive-top: #f1f2df;
    --olive-mid: #a5b052;
    --olive-bottom: #556416;
    --gold-top: #f5ede0;
    --gold-mid: #c29e5c;
    --gold-bottom: #74541a;
    --silver-top: #f4f4f4;
    --silver-mid: #a3a3a3;
    --silver-bottom: #4d4d4d;
    --violet-top: #f5e9f6;
    --violet-mid: #b889c6;
    --violet-bottom: #66357e;
  }
  * { box-sizing: border-box; margin: 0; padding: 0; }
  html, body { width: 1200px; height: 960px; overflow: hidden; }
  body {
    background: var(--canvas-bg);
    font-family: "Montserrat", sans-serif;
    color: var(--ink);
  }
  .label-series {
    position: absolute;
    left: 150px;
    top: 472px;
    display: flex;
    gap: 18px;
  }
  .label {
    position: relative;
    width: 166px;
    height: 400px;
    border-radius: 14px;
    overflow: hidden;
  }
  .label--teal   { background: linear-gradient(180deg, var(--teal-top) 0%, var(--teal-mid) 45%, var(--teal-bottom) 100%); }
  .label--olive  { background: linear-gradient(180deg, var(--olive-top) 0%, var(--olive-mid) 45%, var(--olive-bottom) 100%); }
  .label--gold   { background: linear-gradient(180deg, var(--gold-top) 0%, var(--gold-mid) 45%, var(--gold-bottom) 100%); }
  .label--silver { background: linear-gradient(180deg, var(--silver-top) 0%, var(--silver-mid) 45%, var(--silver-bottom) 100%); }
  .label--violet { background: linear-gradient(180deg, var(--violet-top) 0%, var(--violet-mid) 45%, var(--violet-bottom) 100%); }

  .brand-name {
    position: absolute;
    top: 104px;
    left: 0;
    right: 0;
    text-align: center;
    font-size: 14px;
    font-weight: 400;
    letter-spacing: 1.5px;
    color: var(--ink);
  }
  .product-name {
    position: absolute;
    top: 158px;
    left: 28px;
    font-size: 15.5px;
    font-weight: 300;
    line-height: 16px;
    color: rgba(29, 36, 38, 0.72);
  }
  .product-variant {
    display: block;
    margin-top: 2px;
    font-weight: 400;
    color: var(--white);
    letter-spacing: 0.2px;
  }
  .mark {
    position: absolute;
    top: 290px;
    left: 50%;
    width: 26px;
    height: 26px;
    margin-left: -13px;
    border-radius: 50%;
    background: rgba(255, 255, 255, 0.35);
  }
  .claim {
    position: absolute;
    top: 324px;
    left: 0;
    right: 0;
    text-align: center;
    font-size: 8.5px;
    line-height: 10.5px;
    font-weight: 400;
    color: var(--white);
  }
  .volume {
    position: absolute;
    top: 360px;
    left: 0;
    right: 0;
    text-align: center;
    font-size: 10px;
    font-weight: 300;
    color: rgba(255, 255, 255, 0.85);
  }
</style>
</head>
<body>
  <main class="label-series">
    <article class="label label--teal">
      <div class="brand-name">NORDVIK CARE</div>
      <h2 class="product-name">exfoliating<br>cleanser<span class="product-variant">DEEP ACTION</span></h2>
      <div class="mark" role="img" aria-label="Botanical flower emblem"></div>
      <p class="claim">Naturally Reduces<br>Apperance of Fine Lines</p>
      <p class="volume">100mL &nbsp;℮ 3.39 fl oz</p>
    </article>
    <article class="label label--olive">
      <div class="brand-name">NORDVIK CARE</div>
      <h2 class="product-name">exfoliating<br>cleanser<span class="product-variant">DEEP ACTION</span></h2>
      <div class="mark" role="img" aria-label="Botanical flower emblem"></div>
      <p class="claim">Naturally Reduces<br>Apperance of Fine Lines</p>
      <p class="volume">100mL &nbsp;℮ 3.39 fl oz</p>
    </article>
    <article class="label label--gold">
      <div class="brand-name">NORDVIK CARE</div>
      <h2 class="product-name">exfoliating<br>cleanser<span class="product-variant">DEEP ACTION</span></h2>
      <div class="mark" role="img" aria-label="Botanical flower emblem"></div>
      <p class="claim">Naturally Reduces<br>Apperance of Fine Lines</p>
      <p class="volume">100mL &nbsp;℮ 3.39 fl oz</p>
    </article>
    <article class="label label--silver">
      <div class="brand-name">NORDVIK CARE</div>
      <h2 class="product-name">exfoliating<br>cleanser<span class="product-variant">DEEP ACTION</span></h2>
      <div class="mark" role="img" aria-label="Botanical flower emblem"></div>
      <p class="claim">Naturally Reduces<br>Apperance of Fine Lines</p>
      <p class="volume">100mL &nbsp;℮ 3.39 fl oz</p>
    </article>
    <article class="label label--violet">
      <div class="brand-name">NORDVIK CARE</div>
      <h2 class="product-name">exfoliating<br>cleanser<span class="product-variant">DEEP ACTION</span></h2>
      <div class="mark" role="img" aria-label="Botanical flower emblem"></div>
      <p class="claim">Naturally Reduces<br>Apperance of Fine Lines</p>
      <p class="volume">100mL &nbsp;℮ 3.39 fl oz</p>
    </article>
  </main>
</body>
</html>
```